Organic Soap Packaging

We need a package design for a new company called Willow Naturals. Our primary product is organic soap. Our business model is based on the social entrepreneurial concept of by one give one like Brend shoes. We are giving soap to help prevent the spread of disease; 1.4 million deaths a year can be prevented by hand washing.

The design is for a recycled cardboard box/package. We want to demonstrate the high end, luxury feel of the product with undertones of organic/earth friendly/social conscious.

The soap is small batch, spa like, essential oil scented all natural luxury.
Updates

I am very excited about this startup business and I believe we will have great success! I am passionate about organic personal care and helping others in need. If you share my passion, please bring your work to the table!

Target Market(s)

My target market is people who are educated through college. Health conscious, socially conscious, Generation X. Basically shoppers of Green Basket and Haverline.

Industry/Entity Type

Business

Requirements
Must have
• Suitable for Face, Hair, and Skin
Scented with Organic Essential Oils

```html
<!DOCTYPE html>
<html lang="en">
<head>
<meta charset="utf-8">
<title>Willow Naturals – Organic Soap Packaging</title>
<link rel="stylesheet" href="https://fonts.googleapis.com/css2?family=Encode+Sans+Semi+Condensed:wght@300;400&family=Gochi+Hand&display=swap">
<style>
  :root {
    --page: #ffffff;
    --kraft: #b0946a;
    --kraft-line: #c2a77c;
    --sage-band: #b7cfc4;
    --sage-text: #a08a66;
    --plum: #5e4b4a;
    --cream-script: #efe6c8;
    --butter-band: #e8d98a;
    --butter-text: #a99355;
    --pale-square: #d9cf9a;
    --olive-script: #4f5a26;
    --fine-print: #d8c59c;
  }
  * { margin: 0; padding: 0; box-sizing: border-box; }
  html, body { width: 1200px; height: 900px; overflow: hidden; background: var(--page); }
  .canvas {
    position: relative; width: 1200px; height: 900px;
    font-family: "Encode Sans Semi Condensed", "Arial Narrow", sans-serif;
  }
  .box-front {
    position: absolute; top: 260px; width: 540px; height: 380px;
    background: var(--kraft); overflow: hidden;
  }
  .box-front--sage { left: 40px; }
  .box-front--butter { left: 620px; }
  .leaf-decoration {
    position: absolute; right: 0; top: 0; width: 120px; height: 380px;
    background: linear-gradient(160deg, rgba(194,167,124,0.55), rgba(176,148,106,0));
  }
  .brand-mark {
    position: absolute; left: 36px; top: 110px; width: 70px; height: 150px;
  }
  .brand-name {
    position: absolute; left: 112px; top: 110px; width: 318px; height: 56px;
    font-weight: 300; font-size: 34px; line-height: 56px; padding-left: 12px;
    white-space: nowrap;
  }
  .product-name {
    position: absolute; left: 120px; top: 172px;
    font-family: "Gochi Hand", cursive; font-size: 44px; letter-spacing: 1px;
  }
  .claims {
    position: absolute; left: 118px; top: 250px;
    font-size: 15px; line-height: 21px; color: var(--fine-print); letter-spacing: .3px;
  }
  .box-front--sage .brand-mark { background: var(--plum); }
  .box-front--sage .brand-name { background: var(--sage-band); color: var(--sage-text); }
  .box-front--sage .product-name { color: var(--cream-script); }
  .box-front--butter .brand-mark { background: var(--pale-square); }
  .box-front--butter .brand-name { background: var(--butter-band); color: var(--butter-text); }
  .box-front--butter .product-name { color: var(--olive-script); }
</style>
</head>
<body>
<main class="canvas">
  <section class="box-front box-front--sage">
    <div class="leaf-decoration" role="img" aria-label="Faint line-drawn leaf pattern"></div>
    <div class="brand-mark"></div>
    <h1 class="brand-name">Willow Naturals</h1>
    <p class="product-name">organic soap</p>
    <p class="claims">Suitable for Face, Hair, and Skin<br>Scented with Organic Essential Oils</p>
  </section>
  <section class="box-front box-front--butter">
    <div class="leaf-decoration" role="img" aria-label="Faint line-drawn leaf pattern"></div>
    <div class="brand-mark"></div>
    <h2 class="brand-name">Willow Naturals</h2>
    <p class="product-name">organic soap</p>
    <p class="claims">Suitable for Face, Hair, and Skin<br>Scented with Organic Essential Oils</p>
  </section>
</main>
</body>
</html>
```